Brivora Australia Company Values.

We have just completed our company purpose, beliefs and values (for the first time, we have not had these before)
We are now wanting to add images to each company value as a visual
so they are easily identified and understood for all our staff - we need them to remember the 5 Values.
We are a manufacturer of dental materials and infection control products, based in Melbourne.

What we would like:
- A Poster (that can be placed in our staff lunch rooms)
- The values to be lined up Horizontally
- Image on the top of the words
- Wording does not all need to be the same text font
- No image photographs - please use image graphics
- No images with people
- No dental related graphics

Target audience: Brivora staff

Our Values are:
Think Big
Have a go, learn and adapt
If you're gonna do it, do it bloody well
Empower Others
Be a good human

I have uploaded some examples.

Target Market(s)

Brivora Team members

Industry/Entity Type

Healthcare

Colors

Designer to choose colors to be used in the design.

Requirements
Must have
• Clear horizontal layout, space between each value
Should not have
• No images with humans or dental

```html
<!DOCTYPE html>
<html lang="en">
<head>
<meta charset="utf-8">
<title>Brivora Australia Company Values</title>
<link rel="stylesheet" href="https://fonts.googleapis.com/css2?family=Barlow+Semi+Condensed:wght@700;800&display=swap">
<style>
  :root {
    --stage: #333333;
    --paper: #ffffff;
    --brand-green: #3fb84a;
    --brand-green-soft: #bfe8c3;
    --navy: #172a5e;
    --divider: #cfcfcf;
  }
  html, body {
    margin: 0;
    padding: 0;
    width: 1200px;
    height: 549px;
    overflow: hidden;
    background: var(--stage);
  }
  .values-poster {
    display: block;
    width: 1200px;
    height: 549px;
  }
  .value-text {
    font-family: "Barlow Semi Condensed", "Arial Narrow", sans-serif;
    font-weight: 800;
    fill: var(--navy);
  }
  .value-text--small { font-weight: 700; }
  .poster-frame { fill: var(--paper); }
  .poster-border { fill: none; stroke: var(--brand-green); stroke-width: 12; }
  .value-divider { stroke: var(--divider); stroke-width: 2; stroke-dasharray: 4 4; }
  .value-icon { fill: url(#iconTone); }
</style>
</head>
<body>
<svg class="values-poster" viewBox="0 0 1200 549" xmlns="http://www.w3.org/2000/svg">
  <defs>
    <linearGradient id="iconTone" x1="0" y1="0" x2="0" y2="1">
      <stop offset="0" stop-color="#7fd188"/>
      <stop offset="1" stop-color="#3fb84a"/>
    </linearGradient>
  </defs>

  <rect class="poster-frame" x="106" y="177" width="989" height="194"/>
  <rect class="poster-border" x="120" y="189" width="962" height="171"/>

  <line class="value-divider" x1="257" y1="228" x2="257" y2="321"/>
  <line class="value-divider" x1="429" y1="228" x2="429" y2="321"/>
  <line class="value-divider" x1="682" y1="228" x2="682" y2="321"/>
  <line class="value-divider" x1="891" y1="228" x2="891" y2="321"/>

  <!-- Think Big -->
  <g class="value value--think-big">
    <rect class="value-icon" role="img" aria-label="Green line icon of a brain with spark marks" x="159" y="204" width="60" height="60" rx="8"/>
    <text class="value-text" x="189" y="288" font-size="24" text-anchor="middle">Think</text>
    <text class="value-text" x="192" y="334" font-size="60" text-anchor="middle">BIG</text>
  </g>

  <!-- Have a go, learn & adapt -->
  <g class="value value--learn-adapt">
    <rect class="value-icon" role="img" aria-label="Green line icon of a reader holding an open book" x="315" y="205" width="51" height="59" rx="8"/>
    <text class="value-text value-text--small" x="300" y="282" font-size="17">HAVE A GO,</text>
    <text class="value-text" x="340" y="305" font-size="38" text-anchor="middle">Learn &amp;</text>
    <text class="value-text" x="340" y="335" font-size="38" text-anchor="middle">Adapt</text>
  </g>

  <!-- If you're gonna do it, do it bloody well -->
  <g class="value value--do-it-well">
    <rect class="value-icon" role="img" aria-label="Green icon of two figures giving a high five" x="500" y="204" width="70" height="60" rx="8"/>
    <text class="value-text value-text--small" x="451" y="284" font-size="18">IF YOU'RE</text>
    <text class="value-text value-text--small" x="451" y="300" font-size="18">GONNA DO IT</text>
    <text class="value-text" x="565" y="300" font-size="43">Do It</text>
    <text class="value-text" x="555" y="335" font-size="43" text-anchor="middle">Bloody Well</text>
  </g>

  <!-- Empower others -->
  <g class="value value--empower">
    <rect class="value-icon" role="img" aria-label="Green line icon of a raised fist with spark marks" x="764" y="204" width="50" height="60" rx="8"/>
    <text class="value-text" x="787" y="299" font-size="43" text-anchor="middle">Empower</text>
    <text class="value-text" x="787" y="335" font-size="43" text-anchor="middle">Others</text>
  </g>

  <!-- Be a good human -->
  <g class="value value--good-human">
    <rect class="value-icon" role="img" aria-label="Green line icon of a thumbs up with spark marks" x="956" y="204" width="54" height="60" rx="8"/>
    <text class="value-text value-text--small" x="909" y="300" font-size="20">BE A</text>
    <text class="value-text" x="959" y="298" font-size="43">good</text>
    <text class="value-text" x="982" y="335" font-size="43" text-anchor="middle">human</text>
  </g>
</svg>
</body>
</html>
```